Infographic to explain our offering

We are a cloudrelay.com partner and would like to issue an infographic to our business partners who recommend our services. A one page, A4 graphic, simple and in our colours of blue background and white (clean) images. to cover such things as;

+ UK map (white areas of where we operate)
+ Simple outline icons of the sectors / industries we operate in
+ A simple graphic of number of projects we have completed (500+)
+ A simple graphic of number of years we have been operating (9+)
+ Product areas we work with being, Deal Sphere, Help Sphere, Velmix
+ Services we offer, Consulting to Enterprise and SMB, Training and Support (also, data migration and data integration)
+ Certifications we hold (we have images from Cloudrelay.com that we can incorporate)
+ Broad areas we consult in being, CRM, Marketing Automation and Social Media Engagement
+Maybe something around our specific offerings for SMB market being, QuickLaunch (Bronze, Silver, Gold), showing average days for each. Single Shift Easy Gain

Open to other suggestions

Sectors we operate in;

SMB (up-to £100m)
Professional Services
Marketing / Media
Engineering / Manufacturing
Construction
Healthcare
Financial Services / Investments
Membership

Major UK areas

London (40%)
South East (25%)
Manchester (and surrounding areas) (25%)
Birmingham (and surrounding areas) (10%)

Offices
London
Birmingham
Manchester

More styling ideas and information about our offering and company can be found here

www.harbourvantage.com
Updates

Industry/Entity Type

Business

Font styles to use
Sans Serif

Colors
33a6d7
0692cd
0655a3
ffffff

Requirements
Must have
• Clean and clear messages
Should not have
• Too much text

```html
<!DOCTYPE html>
<html lang="en">
<head>
<meta charset="utf-8">
<title>Infographic Title</title>
<link href="https://fonts.googleapis.com/css2?family=Bebas+Neue&family=Oswald:wght@300;400;500&display=swap" rel="stylesheet">
<style>
:root{
  --navy:#1b4675;
  --deep:#0655a3;
  --mid:#2a72b8;
  --sky:#3a8ccc;
  --light:#33a6d7;
  --bright:#0692cd;
  --pale:#a9d4f0;
  --white:#ffffff;
  --figure:#2b2b2b;
}
*{box-sizing:border-box;margin:0;padding:0}
html,body{width:848px;height:1200px;overflow:hidden;background:var(--white)}
body{position:relative;font-family:"Oswald",sans-serif;color:var(--white)}
.abs{position:absolute}
.header{top:0;left:0;width:848px;height:124px;text-align:center}
.header h1{font-family:"Bebas Neue",sans-serif;font-weight:400;font-size:64px;letter-spacing:2px;color:var(--navy);line-height:1;padding-top:20px}
.header p{font-size:16px;color:var(--bright);font-weight:300;margin-top:2px}
.panel{left:0;width:848px}
.solutions{top:131px;height:362px;background:var(--deep)}
.products{top:505px;height:216px;background:var(--mid)}
.services{top:733px;height:350px;background:var(--sky)}
.panel h2{position:absolute;left:96px;top:20px;font-family:"Bebas Neue",sans-serif;font-weight:400;font-size:58px;letter-spacing:2px;line-height:1;z-index:1}
.panel svg{position:absolute;left:0;top:0}
.label{font-family:"Oswald",sans-serif;font-weight:400;fill:var(--white)}
.num{font-family:"Oswald",sans-serif;font-weight:300;font-size:64px;fill:none;stroke:var(--pale);stroke-width:1.5}
.caption{font-family:"Oswald",sans-serif;font-size:19px;fill:var(--white)}
.footer{top:1110px;left:0;width:848px;display:flex;justify-content:center;align-items:center;gap:14px;font-family:"Bebas Neue",sans-serif;font-size:48px;letter-spacing:2px;color:var(--light)}
</style>
</head>
<body>

<header class="header abs">
  <h1>Infographic Title</h1>
  <p>Lorem ipsum dolor sit amet, Lorem ipsum dolor sit amet</p>
</header>

<section class="panel solutions abs">
  <h2>Solutions For</h2>
  <svg width="848" height="362" viewBox="0 0 848 362">
    <defs>
      <linearGradient id="figureTone" x1="0" y1="0" x2="0" y2="1">
        <stop offset="0" stop-color="#2b2b2b" stop-opacity=".55"/>
        <stop offset="1" stop-color="#2b2b2b" stop-opacity=".2"/>
      </linearGradient>
      <linearGradient id="mapTone" x1="0" y1="0" x2="0" y2="1">
        <stop offset="0" stop-color="#ffffff" stop-opacity=".95"/>
        <stop offset="1" stop-color="#ffffff" stop-opacity=".75"/>
      </linearGradient>
    </defs>
    <!-- figure areas -->
    <rect x="40" y="150" width="100" height="180" rx="10" fill="url(#figureTone)" role="img" aria-label="Person holding up the years operating badge"/>
    <rect x="708" y="150" width="100" height="180" rx="10" fill="url(#figureTone)" role="img" aria-label="Person holding up the projects completed badge"/>
    <circle cx="117" cy="155" r="34" fill="var(--light)"/>
    <text class="label" x="117" y="155" text-anchor="middle" font-size="18">9+</text>
    <text class="label" x="117" y="171" text-anchor="middle" font-size="8">YEARS OPERATING</text>
    <circle cx="731" cy="145" r="36" fill="var(--light)"/>
    <text class="label" x="731" y="145" text-anchor="middle" font-size="18">500+</text>
    <text class="label" x="731" y="161" text-anchor="middle" font-size="8">PROJECTS COMPLETED</text>
    <!-- connector lines and arc -->
    <g stroke="var(--white)" stroke-width="1.5" fill="none" opacity=".8">
      <path d="M205 125 V150 H330"/>
      <path d="M520 150 H645 V125"/>
    </g>
    <path d="M290 225 Q424 345 558 225" stroke="var(--bright)" stroke-width="14" fill="none" opacity=".7"/>
    <!-- map area -->
    <rect x="388" y="104" width="112" height="142" rx="12" fill="url(#mapTone)" role="img" aria-label="Map of the UK with operating regions shown in white"/>
    <g class="label" text-anchor="middle" font-size="8">
      <circle cx="362" cy="165" r="24" fill="var(--navy)"/><text x="362" y="162">MANCHESTER</text><text x="362" y="174">25%</text>
      <circle cx="362" cy="228" r="24" fill="var(--navy)"/><text x="362" y="225">BIRMINGHAM</text><text x="362" y="237">10%</text>
      <circle cx="478" cy="162" r="26" fill="var(--navy)"/><text x="478" y="158">LONDON</text><text x="478" y="171">40%</text>
      <circle cx="505" cy="208" r="24" fill="var(--navy)"/><text x="505" y="205">SOUTHEAST</text><text x="505" y="217">25%</text>
    </g>
    <!-- sector icons -->
    <g fill="none" stroke="var(--white)" stroke-width="2">
      <circle cx="225" cy="137" r="6"/><circle cx="240" cy="125" r="6"/><circle cx="240" cy="150" r="6"/>
      <path d="M203 269 h8 l5 -10 l6 20 l5 -10 h8"/>
      <rect x="292" y="270" width="22" height="16"/><path d="M296 270 v-6 h14 v6"/>
      <rect x="505" y="272" width="10" height="18"/><rect x="518" y="264" width="10" height="26"/>
      <circle cx="623" cy="128" r="5"/><circle cx="641" cy="128" r="5"/><path d="M616 145 q7-10 14 0 M634 145 q7-10 14 0"/>
      <path d="M660 282 v-18 l10 6 v-6 l10 6 v-10 h6 v22 z"/>
    </g>
    <g class="label" font-size="9" opacity=".9">
      <text x="205" y="168">STRATEGY &amp; PLAN</text>
      <text x="188" y="300">HEALTHCARE</text>
      <text x="262" y="302">FINANCIAL &amp; INVESTMENT</text>
      <text x="494" y="305">CONSTRUCTION</text>
      <text x="598" y="168">MARKETING/MEDIA</text>
      <text x="620" y="300">ENGINEERING/MANUFACTURING</text>
    </g>
  </svg>
</section>

<section class="panel products abs">
  <h2>Product Areas</h2>
  <svg width="848" height="216" viewBox="0 0 848 216">
    <g stroke="var(--pale)" stroke-width="2">
      <path d="M335 152 H436"/><path d="M514 152 H582"/><path d="M660 152 H724"/>
    </g>
    <circle cx="335" cy="152" r="3" fill="var(--pale)"/>
    <g fill="var(--white)">
      <circle cx="475" cy="63" r="28"/><circle cx="621" cy="63" r="28"/><circle cx="763" cy="63" r="28"/>
    </g>
    <g fill="none" stroke="var(--deep)" stroke-width="2.5">
      <rect x="466" y="48" width="18" height="30" rx="3"/><path d="M477 54 l-5 9 h6 l-5 9"/>
      <rect x="606" y="53" width="18" height="16"/><path d="M624 58 h8 l4 6 v5 h-12"/><circle cx="611" cy="71" r="3"/><circle cx="630" cy="71" r="3"/>
      <circle cx="757" cy="58" r="7"/><circle cx="771" cy="70" r="5"/>
    </g>
    <text class="num" x="475" y="175" text-anchor="middle">01</text>
    <text class="num" x="621" y="175" text-anchor="middle">02</text>
    <text class="num" x="763" y="175" text-anchor="middle">03</text>
    <text class="caption" x="475" y="198" text-anchor="middle">DEAL SPHERE</text>
    <text class="caption" x="621" y="198" text-anchor="middle">HELP SPHERE</text>
    <text class="caption" x="763" y="198" text-anchor="middle">VELMIX</text>
  </svg>
</section>

<section class="panel services abs">
  <h2>Services</h2>
  <svg width="848" height="350" viewBox="0 0 848 350">
    <g stroke="var(--pale)" stroke-width="2">
      <path d="M410 137 H436"/><path d="M514 137 H582"/>
    </g>
    <g fill="var(--bright)"><circle cx="475" cy="51" r="30"/><circle cx="621" cy="51" r="30"/></g>
    <g fill="var(--white)">
      <circle cx="470" cy="44" r="8"/><path d="M456 66 q14-20 28 0z"/><circle cx="487" cy="52" r="5"/>
      <circle cx="608" cy="48" r="6"/><circle cx="621" cy="42" r="7"/><circle cx="634" cy="48" r="6"/><path d="M598 66 q23-24 46 0z"/>
    </g>
    <text class="num" x="475" y="160" text-anchor="middle">01</text>
    <text class="num" x="621" y="160" text-anchor="middle">02</text>
    <text class="caption" x="475" y="183" text-anchor="middle">CONSULTING</text>
    <text class="caption" x="621" y="183" text-anchor="middle">TRAINING + SUPPORT</text>
    <text class="caption" x="621" y="206" text-anchor="middle" font-size="16">+</text>
    <text class="caption" x="621" y="230" text-anchor="middle" font-size="17">(and data analysis)</text>
    <rect x="660" y="245" width="36" height="30" fill="var(--white)"/>
    <path d="M664 270 l8-8 l8 4 l12-12" stroke="var(--deep)" stroke-width="2" fill="none"/>
    <!-- enterprise -->
    <circle cx="180" cy="157" r="38" fill="var(--deep)"/>
    <circle cx="180" cy="143" r="10" fill="none" stroke="var(--white)" stroke-width="2"/>
    <rect x="162" y="160" width="36" height="16" fill="none" stroke="var(--white)" stroke-width="2"/>
    <text class="label" x="180" y="172" text-anchor="middle" font-size="9">CEO</text>
    <g class="label" font-size="15">
      <text x="233" y="140" font-weight="500">ENTERPRISES</text>
      <text x="233" y="158">CRM</text><text x="233" y="176">Marketing</text><text x="233" y="194">Social Media</text>
      <text x="233" y="234" font-weight="500">SMALL BUSINESS</text><text x="233" y="252">QuickLaunch</text>
    </g>
    <!-- small business -->
    <circle cx="180" cy="263" r="38" fill="var(--bright)"/>
    <rect x="160" y="258" width="40" height="16" rx="3" fill="none" stroke="var(--white)" stroke-width="2"/>
    <text class="label" x="180" y="270" text-anchor="middle" font-size="9">OPEN</text>
    <g fill="var(--light)" stroke="var(--pale)">
      <circle cx="254" cy="287" r="21"/><circle cx="307" cy="287" r="21"/><circle cx="356" cy="287" r="21"/>
    </g>
    <g class="label" font-size="7" text-anchor="middle">
      <text x="254" y="290">BRONZE</text><text x="307" y="290">SILVER</text><text x="356" y="290">GOLD</text>
    </g>
  </svg>
</section>

<footer class="footer abs">
  <svg width="34" height="36" viewBox="0 0 34 36" aria-hidden="true">
    <rect x="2" y="4" width="20" height="32" fill="var(--light)"/><rect x="22" y="14" width="10" height="22" fill="var(--light)"/>
    <g fill="var(--white)"><rect x="6" y="9" width="4" height="4"/><rect x="14" y="9" width="4" height="4"/><rect x="6" y="17" width="4" height="4"/><rect x="14" y="17" width="4" height="4"/><rect x="6" y="25" width="4" height="4"/><rect x="14" y="25" width="4" height="4"/></g>
  </svg>
  <span>Offices London/Birmingham/Manchester</span>
</footer>

</body>
</html>
```